Communication and Marketing agency needs a new presentation card

We are a group of communication and marketing agencies specialized in companies that are in the logistics and industrial sector. The head agency is TELVANO Grupo and the group consists of 4 agencies: TELVANO Media, TELVANO Digital, TELVANO Research and EnlazaPorImagen. We hace 4 offices in Spain (Madrid, Barcelona, Valencia and Murcia). We are looking for a clean and attractive design that transmits our experience, brand presence in the market and knowledge to those who receive the card.It has to maintain the colors of the logo that is attached.
Target Market(s)
logistics and industrial sector
Marketing department
Clean and attractive design

```html
<!DOCTYPE html>
<html lang="es">
<head>
<meta charset="utf-8">
<title>TELVANO Grupo – Tarjeta de presentación</title>
<link rel="stylesheet" href="https://fonts.googleapis.com/css2?family=Josefin+Sans:wght@300;400&display=swap">
<style>
  :root {
    --brand-red: #a91c27;
    --card-black: #1f1d1e;
    --steel-grey: #5c5c5e;
    --soft-grey: #7a7a7c;
    --page-bg: #e8e5e1;
    --brand-font: "Josefin Sans", sans-serif;
  }
  * { margin: 0; padding: 0; box-sizing: border-box; }
  html, body { width: 1200px; height: 900px; overflow: hidden; }
  body { background: var(--page-bg); font-family: var(--brand-font); position: relative; }

  .card {
    position: absolute; left: 250px; width: 700px; height: 400px;
    background: var(--card-black); overflow: hidden;
    box-shadow: 0 6px 18px rgba(0,0,0,.18);
  }
  .card--back { top: 40px; }
  .card--front { top: 470px; }
  .card-shapes { position: absolute; inset: 0; }

  .wordmark {
    position: absolute; font-weight: 300; line-height: 1;
    text-transform: none; letter-spacing: .04em;
  }
  .wordmark__name { display: block; text-transform: uppercase; letter-spacing: .06em; }
  .wordmark__unit { display: block; text-align: right; font-size: .45em; margin-top: .15em; letter-spacing: .03em; }
  .wordmark--red { color: var(--brand-red); }
  .wordmark--grey { color: var(--soft-grey); }

  .back-logo { left: 455px; top: 128px; font-size: 38px; }
  .back-website {
    position: absolute; left: 455px; top: 332px; font-size: 13px;
    letter-spacing: .32em; color: var(--brand-red); font-weight: 300;
  }

  .front-logo { left: 50%; top: 182px; transform: translateX(-50%); font-size: 50px; }

  .agency-row {
    position: absolute; left: 40px; right: 60px; top: 315px;
    display: flex; justify-content: space-between; align-items: flex-start;
  }
  .agency-row .wordmark { position: static; font-size: 26px; }
  .agency-split { display: block; font-size: 24px; letter-spacing: .04em; text-transform: uppercase; line-height: 1.05; }
</style>
</head>
<body>

  <section class="card card--back" aria-label="Reverso de la tarjeta">
    <svg class="card-shapes" viewBox="0 0 700 400" aria-hidden="true">
      <path fill="var(--brand-red)"
            d="M0,0 H300 C330,0 330,42 362,42 H402 Q432,42 432,72 V368 Q432,400 400,400 H0 Z"/>
    </svg>
    <div class="wordmark wordmark--red back-logo">
      <span class="wordmark__name">Telvano</span>
      <span class="wordmark__unit">Grupo</span>
    </div>
    <p class="back-website">www.telvano-grupo.es</p>
  </section>

  <section class="card card--front" aria-label="Anverso de la tarjeta">
    <svg class="card-shapes" viewBox="0 0 700 400" aria-hidden="true">
      <polyline fill="none" stroke="var(--brand-red)" stroke-width="16" stroke-linejoin="miter"
                points="0,46 328,12 372,122 672,30 672,400"/>
      <polyline fill="none" stroke="var(--steel-grey)" stroke-width="5" stroke-linejoin="miter"
                points="0,60 318,28 360,136 656,50 656,400"/>
    </svg>

    <div class="wordmark wordmark--red front-logo">
      <span class="wordmark__name">Telvano</span>
      <span class="wordmark__unit">Grupo</span>
    </div>

    <div class="agency-row">
      <div class="wordmark wordmark--red">
        <span class="wordmark__name">Telvano</span>
        <span class="wordmark__unit">Media</span>
      </div>
      <div class="wordmark wordmark--red">
        <span class="agency-split">Enlaza</span>
        <span class="agency-split">PorImagen</span>
      </div>
      <div class="wordmark wordmark--grey">
        <span class="wordmark__name">Telvano</span>
        <span class="wordmark__unit">Digital</span>
      </div>
      <div class="wordmark wordmark--grey">
        <span class="wordmark__name">Telvano</span>
        <span class="wordmark__unit">Research</span>
      </div>
    </div>
  </section>

</body>
</html>
```